The Morrow Ledgers Website

I need a website to help promote the series of science fiction novels that I am in the process of writing.

I have some content and photos and am in the process of getting some new book cover artwork designed.

I have a current website/domain etc http://www.vantorpagehouse.co.nz but I need something a little more professional and eye catchig but I also want to be able to manage the content myself.

I can send e-versions of the two completed novels for context to any takers

```html
<!DOCTYPE html>
<html lang="en">
<head>
<meta charset="utf-8">
<title>The Morrow Ledgers</title>
<link href="https://fonts.googleapis.com/css2?family=Open+Sans:wght@600&family=Raleway:wght@400&family=Oswald:wght@400&display=swap" rel="stylesheet">
<style>
  :root {
    --accent: #1a9fe0;
    --ink: #1e1e1e;
    --muted: #9a9a9a;
    --line-grey: #b9b9b9;
    --paper: #ffffff;
    --suit-dark: #2a2a22;
    --suit-mid: #4a4538;
    --cover-teal: #2c4c5c;
    --cover-teal-dark: #17303c;
    --cover-space: #1c201a;
    --cover-space-light: #4a4a30;
  }
  * { margin: 0; padding: 0; box-sizing: border-box; }
  html, body { width: 1200px; height: 900px; overflow: hidden; background: var(--paper); }
  .page { position: relative; width: 1200px; height: 900px; overflow: hidden; }

  .review { position: absolute; left: 100px; width: 583px; height: 223px; }
  .review--active .review-frame { position: absolute; left: 0; top: 0; }
  .review-icon { position: absolute; left: 21px; top: 30px; width: 100px; height: 100px; }
  .review-author {
    position: absolute; left: 149px; top: 27px;
    font: 600 20px/1.2 "Open Sans", sans-serif; color: var(--ink);
  }
  .review-text {
    position: absolute; left: 149px; top: 72px; width: 420px;
    font: 400 16px/22.5px "Raleway", sans-serif; color: var(--muted);
  }
  .review-more {
    position: absolute; right: 42px;
    font: 400 18px/1 "Raleway", sans-serif; color: var(--ink); text-decoration: none;
  }
  .review--active .review-more { color: var(--accent); }

  .author-photo {
    position: absolute; left: 795px; top: 0; width: 220px; height: 662px;
    border-radius: 60px 60px 30px 30px;
    background: linear-gradient(180deg, #d9c2a8 0%, #d9c2a8 14%, var(--suit-mid) 18%, var(--suit-dark) 60%, #3a2a22 100%);
  }

  .books-title {
    position: absolute; left: 0; width: 1200px; top: 742px; text-align: center;
    font: 400 36px/1.2 "Oswald", sans-serif; color: #000; letter-spacing: -0.5px;
  }
  .books-nav { position: absolute; top: 748px; width: 42px; height: 42px; background: var(--paper); border: 1px solid var(--line-grey); border-radius: 3px; }
  .books-nav--prev { left: 1007px; }
  .books-nav--next { left: 1059px; border-color: var(--accent); }
  .books-nav svg { display: block; }

  .book-cover { position: absolute; top: 828px; width: 235px; height: 72px; }
  .book-cover--teal { background: linear-gradient(180deg, var(--cover-teal-dark), var(--cover-teal)); }
  .book-cover--space { background: radial-gradient(ellipse at 50% 80%, var(--cover-space-light), var(--cover-space) 70%); }
</style>
</head>
<body>
<main class="page">

  <section class="review review--active" style="top:18px">
    <svg class="review-frame" width="640" height="223" viewBox="0 0 640 223">
      <path d="M5 1 H577 Q582 1 582 6 V75 L635 106 L582 138 V217 Q582 222 577 222 H5 Q1 222 1 217 V6 Q1 1 5 1 Z" fill="none" stroke="var(--accent)" stroke-width="2"/>
    </svg>
    <svg class="review-icon" viewBox="0 0 100 100">
      <circle cx="50" cy="50" r="46.5" fill="none" stroke="var(--accent)" stroke-width="5"/>
      <path d="M50 36 H37 V64 H63 V51" fill="none" stroke="var(--accent)" stroke-width="4"/>
      <path d="M46 55 L47 48 L61 34 L66 39 L52 53 Z" fill="var(--accent)"/>
    </svg>
    <h3 class="review-author">By Marlow Teague</h3>
    <p class="review-text">There is a reasonable story there which takes a while to get going to a emotive level , but about half way through all seems to flow&nbsp; better as the author get comfortable with the characters and has a handle on where the story is going.</p>
    <a class="review-more" href="#" style="top:183px">read more</a>
  </section>

  <section class="review" style="top:261px">
    <svg class="review-icon" viewBox="0 0 100 100">
      <circle cx="50" cy="50" r="46.5" fill="none" stroke="var(--accent)" stroke-width="5"/>
      <path d="M36 36 H68 Q72 36 72 40 H64 V64 H30 V58 H60 V40 Q60 36 56 36" fill="var(--accent)"/>
      <path d="M34 40 L46 52 L43 55 L31 43 Z" fill="var(--accent)"/>
      <path d="M40 52 H56 M44 47 H56" stroke="var(--paper)" stroke-width="2"/>
    </svg>
    <h3 class="review-author">By R Ostrovan</h3>
    <p class="review-text">Interesting and easy to read. Alden keeps the suspense through rich descriptions and engaging conversations. Themes of environmental awareness and spiritual discoveries are especially relevant to today's Western culture.</p>
    <a class="review-more" href="#" style="top:183px">read more</a>
  </section>

  <section class="review" style="top:504px">
    <svg class="review-icon" viewBox="0 0 100 100">
      <circle cx="50" cy="50" r="46.5" fill="none" stroke="var(--accent)" stroke-width="5"/>
      <path d="M33 31 H55 L63 39 V48 M63 62 V69 H33 Z" fill="none" stroke="var(--accent)" stroke-width="3"/>
      <path d="M39 45 H52 M39 51 H50 M39 57 H46" stroke="var(--accent)" stroke-width="2.5"/>
      <path d="M50 63 L52 57 L68 41 L73 46 L57 62 Z" fill="var(--accent)"/>
    </svg>
    <h3 class="review-author">By Priya L Wenham</h3>
    <p class="review-text">This book had me captivated from start to end. It had a perfect mixture of humour and sci-fi with fantastic, well developed characters. Can't wait for the next book in the series!</p>
    <a class="review-more" href="#" style="top:163px">read more</a>
  </section>

  <div class="author-photo" role="img" aria-label="Photo of the author standing in a dark suit and tie"></div>

  <h2 class="books-title">Our Books</h2>
  <a class="books-nav books-nav--prev" href="#" aria-label="Previous">
    <svg width="40" height="40" viewBox="0 0 40 40"><path d="M25 9 L14 20 L25 31" fill="none" stroke="var(--line-grey)" stroke-width="1.5"/></svg>
  </a>
  <a class="books-nav books-nav--next" href="#" aria-label="Next">
    <svg width="40" height="40" viewBox="0 0 40 40"><path d="M15 9 L26 20 L15 31" fill="none" stroke="var(--accent)" stroke-width="1.5"/></svg>
  </a>

  <div class="book-cover book-cover--teal" style="left:101px" role="img" aria-label="Book cover artwork, first novel"></div>
  <div class="book-cover book-cover--space" style="left:356px" role="img" aria-label="Book cover artwork, second novel"></div>
  <div class="book-cover book-cover--teal" style="left:611px" role="img" aria-label="Book cover artwork, first novel"></div>
  <div class="book-cover book-cover--space" style="left:866px" role="img" aria-label="Book cover artwork, second novel"></div>

</main>
</body>
</html>
```